Bref créative
BRISK FIELD Stationery
Stationery for BRISKFIELD web site
Professional
Tomas Kerbrune
7 Rue Montaleur, Res. Les Pins
Hendaye
info@briskfield-exemple.com
www.briskfield-exemple.com

```html
<!DOCTYPE html>
<html lang="fr">
<head>
<meta charset="utf-8">
<title>BRISK FIELD Stationery</title>
<link href="https://fonts.googleapis.com/css2?family=Roboto+Condensed:wght@400;700&display=swap" rel="stylesheet">
<style>
:root{
  --bg-light:#f2f2f2;
  --bg-mid:#d9d9d9;
  --ink:#1a1a1a;
  --ink-soft:#555;
  --paper:#ffffff;
  --dark:#141414;
  --dark-2:#2b2b2b;
  --orange:#e2541a;
  --orange-deep:#a8260c;
  --red:#c8241a;
  --caption:#8a8a8a;
}
*{box-sizing:border-box;margin:0;padding:0}
html,body{width:1200px;height:389px;overflow:hidden}
body{
  position:relative;
  font-family:"Roboto Condensed",Arial,sans-serif;
  background:radial-gradient(ellipse at 15% 30%,var(--bg-light),var(--bg-mid) 90%);
  color:var(--ink);
}
.piece{position:absolute;box-shadow:0 3px 8px rgba(0,0,0,.35)}
.caption{position:absolute;font-size:7px;color:var(--caption);text-align:center;width:100%;bottom:-11px;left:0}
.wordmark{font-weight:700;letter-spacing:.5px;display:flex;align-items:center;gap:5px;white-space:nowrap}
.wordmark .dot{border-radius:50%;background:var(--orange);display:inline-block}

/* title block */
.title-block{position:absolute;left:48px;top:72px}
.title-block .wordmark{font-size:30px;color:var(--dark-2)}
.title-block .wordmark .dot{width:30px;height:30px}
.title-block .subtitle{font-size:13px;color:var(--ink-soft);margin:6px 0 0 36px}

/* business cards */
.card{width:152px;height:72px;background:linear-gradient(160deg,var(--dark-2),var(--dark))}
.card .wordmark{color:#fff;font-size:12px;position:absolute}
.card .wordmark .dot{width:12px;height:12px}
.card-info{position:absolute;font-size:5.5px;line-height:8px;color:#ddd;right:8px;top:30px;text-align:right}
.card-info b{color:var(--orange);font-size:7px}
.card--orange{background:radial-gradient(ellipse at 50% 50%,var(--orange),var(--orange-deep) 95%)}

/* letterheads */
.letterhead{width:245px;height:352px;background:var(--paper)}
.letterhead .head{position:absolute;left:94px;top:8px;width:60px;height:18px;background:var(--dark);display:flex;align-items:center;justify-content:center}
.letterhead .head .wordmark{color:#fff;font-size:7px;gap:3px}
.letterhead .head .dot{width:7px;height:7px}
.letterhead .contact{position:absolute;left:165px;top:9px;font-size:4.5px;line-height:6px;color:var(--red)}
.letterhead .mark{position:absolute;left:72px;top:130px;width:100px;height:100px;border-radius:50%;background:radial-gradient(circle,#f2dcd6,#f7f0ee 70%);opacity:.8}
.letterhead .foot{position:absolute;left:0;bottom:8px;width:100%;height:3px;background:linear-gradient(90deg,var(--orange-deep),var(--orange),#ddd)}

/* envelopes */
.envelope{width:312px;height:150px;background:var(--paper)}
.envelope--orange{background:radial-gradient(ellipse at 50% 25%,var(--orange),var(--orange-deep) 95%)}
.envelope svg{position:absolute;left:0;top:0}
.seal{position:absolute;left:146px;width:20px;height:20px;border-radius:50%;background:var(--dark)}

/* compliment slip */
.slip{width:312px;height:132px;background:var(--paper)}
.slip .head{position:absolute;left:4px;top:6px;width:84px;height:22px;background:var(--dark);display:flex;align-items:center;justify-content:center}
.slip .head .wordmark{color:#fff;font-size:9px;gap:3px}
.slip .head .dot{width:8px;height:8px}
.slip .mark{position:absolute;left:126px;top:38px;width:64px;height:64px;border-radius:50%;background:radial-gradient(circle,#f2dcd6,#f8f2f0 70%)}
.slip .foot{position:absolute;left:0;bottom:6px;width:100%;height:3px;background:linear-gradient(90deg,var(--orange-deep),var(--orange),#ddd)}
</style>
</head>
<body>

<section class="title-block">
  <div class="wordmark"><span class="dot"></span>BRISKFIELD</div>
  <p class="subtitle">Stationery Concepts</p>
</section>

<!-- business cards -->
<div class="piece card" style="left:12px;top:160px">
  <div class="wordmark" style="left:8px;top:12px"><span class="dot"></span>BRISKFIELD</div>
  <div class="card-info"><b>Tomas Kerbrune</b><br>7 Rue Montaleur, Res. Les Pins<br>+33 5 59 00 41 27<br>info@briskfield-exemple.com</div>
  <span class="caption">Card front 01</span>
</div>
<div class="piece card" style="left:173px;top:160px">
  <div class="wordmark" style="left:8px;top:12px"><span class="dot"></span>BRISKFIELD</div>
  <div class="card-info" style="top:40px">www.briskfield-exemple.com<br>skype: tomkerb</div>
  <span class="caption">Card back 01</span>
</div>
<div class="piece card" style="left:12px;top:262px">
  <div class="wordmark" style="left:44px;top:29px;font-size:10px"><span class="dot" style="width:10px;height:10px"></span>BRISKFIELD</div>
  <span class="caption">Card front 02</span>
</div>
<div class="piece card card--orange" style="left:173px;top:262px">
  <div class="card-info" style="color:#fff;top:26px">Tomas Kerbrune<br>www.briskfield-exemple.com</div>
  <span class="caption">Card back 02</span>
</div>

<!-- letterheads -->
<div class="piece letterhead" style="left:343px;top:15px">
  <div class="head"><div class="wordmark"><span class="dot"></span>BRISKFIELD</div></div>
  <div class="contact">7 Rue Montaleur, Res. Les Pins<br>64700 Hendaye<br>+33 5 59 00 41 27<br>info@briskfield-exemple.com<br>www.briskfield-exemple.com</div>
  <div class="mark" role="img" aria-label="Faint brand circle"></div>
  <div class="foot"></div>
  <span class="caption">Letterhead 01</span>
</div>
<div class="piece letterhead" style="left:612px;top:15px">
  <div class="head"><div class="wordmark"><span class="dot"></span>BRISKFIELD</div></div>
  <div class="mark" role="img" aria-label="Faint brand circle"></div>
  <div class="foot"></div>
  <span class="caption">Letterhead 02</span>
</div>

<!-- envelopes -->
<div class="piece envelope envelope--orange" style="left:876px;top:12px">
  <div class="seal" style="top:50px"></div>
</div>
<div class="piece envelope" style="left:876px;top:96px;height:120px">
  <svg width="312" height="120" viewBox="0 0 312 120"><path d="M0 0 L156 64 L312 0" fill="none" stroke="#d0d0d0" stroke-width="1"/></svg>
  <div class="seal" style="top:54px"></div>
  <span class="caption">Envelope</span>
</div>

<!-- compliment slip -->
<div class="piece slip" style="left:876px;top:232px">
  <div class="head"><div class="wordmark"><span class="dot"></span>BRISKFIELD</div></div>
  <div class="mark" role="img" aria-label="Faint brand circle"></div>
  <div class="foot"></div>
  <span class="caption">Compliment slip</span>
</div>

</body>
</html>
```